Looking for awesome business card design with attached existing logo

We are a water, mold, and fire damage restoration company called "Torvane Seco" Looking for an awesome business card that is edgy yet professional and unique. Show me what you got!

```html
<!DOCTYPE html>
<html lang="en">
<head>
<meta charset="UTF-8">
<title>Torvane Seco — Business Card</title>
<link rel="stylesheet" href="https://fonts.googleapis.com/css2?family=Montserrat:wght@500;600;700;800&display=swap">
<style>
  :root {
    --navy: #24495a;
    --gold: #e0991b;
    --paper: #ffffff;
    --stage: #3a3d40;
    --edge: #c98a1a;
  }
  * { margin: 0; padding: 0; box-sizing: border-box; }
  html, body { width: 1200px; height: 939px; overflow: hidden; }
  body {
    background: var(--stage);
    font-family: "Montserrat", sans-serif;
    position: relative;
  }
  .card {
    position: absolute;
    left: 280px;
    width: 640px;
    height: 366px;
    background: var(--paper);
    border-bottom: 4px solid var(--edge);
    box-shadow: 0 12px 30px rgba(0,0,0,.45);
  }
  .card--front { top: 70px; }
  .card--back { top: 500px; }

  .wordmark {
    color: var(--navy);
    font-weight: 800;
    letter-spacing: 1px;
    text-transform: uppercase;
    display: flex;
    align-items: center;
    gap: 12px;
    white-space: nowrap;
  }
  .wordmark__dot {
    width: 14px; height: 14px;
    border-radius: 50%;
    background: var(--gold);
    flex: none;
  }
  .card--front .wordmark {
    position: absolute;
    left: 50%; top: 50%;
    transform: translate(-50%, -50%);
    font-size: 44px;
  }
  .card--back .wordmark {
    position: absolute;
    left: 34px; top: 150px;
    font-size: 27px;
  }

  .divider {
    position: absolute;
    left: 322px; top: 58px;
    width: 2px; height: 190px;
    display: flex; flex-direction: column;
  }
  .divider span { display: block; width: 2px; }
  .divider .seg-navy { background: var(--navy); height: 36px; }
  .divider .seg-gold { background: var(--gold); height: 100px; margin: 8px 0; }

  .contact {
    position: absolute;
    left: 350px; top: 52px;
    color: var(--navy);
  }
  .contact__name {
    color: var(--gold);
    font-weight: 700;
    font-size: 22px;
    letter-spacing: .5px;
    text-transform: uppercase;
  }
  .contact__role { font-weight: 600; font-size: 13px; margin-top: 2px; }
  .contact__address { font-weight: 500; font-size: 13px; line-height: 18px; margin-top: 14px; }
  .contact__list { list-style: none; margin-top: 12px; font-size: 13px; font-weight: 500; }
  .contact__list li { display: flex; align-items: center; gap: 7px; line-height: 21px; }
  .contact__list svg { width: 11px; height: 11px; fill: var(--gold); flex: none; }
  .hl { color: var(--gold); }

  .services {
    position: absolute;
    right: 44px; bottom: 38px;
    color: var(--navy);
    font-weight: 600;
    font-size: 17px;
    letter-spacing: .5px;
    display: flex; gap: 8px; align-items: center;
  }
  .services__sep { width: 3px; height: 17px; background: var(--gold); }
</style>
</head>
<body>
  <section class="card card--front" aria-label="Card front">
    <div class="wordmark"><span class="wordmark__dot"></span>Torvane Seco</div>
  </section>

  <section class="card card--back" aria-label="Card back">
    <div class="wordmark"><span class="wordmark__dot"></span>Torvane Seco</div>

    <div class="divider" aria-hidden="true">
      <span class="seg-navy"></span><span class="seg-gold"></span><span class="seg-navy"></span>
    </div>

    <div class="contact">
      <p class="contact__name">Daniel Marsh</p>
      <p class="contact__role">Founder and President</p>
      <p class="contact__address">48 Harlow Avenue, Ground Floor<br>Brookfield, NY 10452</p>
      <ul class="contact__list">
        <li><svg viewBox="0 0 24 24"><path d="M6.6 10.8a15 15 0 0 0 6.6 6.6l2.2-2.2c.3-.3.7-.4 1-.2 1.1.4 2.3.6 3.6.6.6 0 1 .4 1 1V20c0 .6-.4 1-1 1A17 17 0 0 1 3 4c0-.6.4-1 1-1h3.5c.6 0 1 .4 1 1 0 1.3.2 2.5.6 3.6.1.3 0 .7-.2 1z"/></svg>+1 (555) 014-2290</li>
        <li><svg viewBox="0 0 24 24"><path d="M2 5h20v14H2z M2 5l10 8 10-8" /></svg>info@<span class="hl">torvaneseco</span>.com</li>
        <li><svg viewBox="0 0 24 24"><circle cx="12" cy="12" r="10"/></svg>www.<span class="hl">torvaneseco</span>.com</li>
      </ul>
    </div>

    <div class="services">
      <span>WATER</span><span class="services__sep"></span>
      <span>MOLD</span><span class="services__sep"></span>
      <span>FIRE</span>
    </div>
  </section>
</body>
</html>
```